Cover Page for Pixelwall, Workbridge & Dwellora.com

I'm needing a cover page for Pixelwall, Workbridge & Dwellora.com. I already have my logo and some samples of what I'm looking for but open to new ideals. I'm in the real estate business and want something that looks very professional and clean. The area I cover is located in the Lake Norman area of North Carolina so would like to incorporate a lake background along with my logo, headshot and contact information.

```html
<!DOCTYPE html>
<html lang="en">
<head>
<meta charset="utf-8">
<title>Mark Delaney – Broker | Realtor Cover</title>
<link href="https://fonts.googleapis.com/css2?family=Montserrat:wght@600;700&family=Poppins:wght@600;700&display=swap" rel="stylesheet">
<style>
  :root {
    --backdrop: #b9a8a6;
    --ink: #1b1a1c;
    --navy-dark: #0a0b18;
    --green: #0e9150;
    --green-deep: #077a40;
    --green-soft: #8fce97;
    --sky-top: #f47b6a;
    --sky-mid: #f39a5c;
    --dusk: #a9685a;
    --portrait-tone: #56627a;
    --white: #ffffff;
    --gold: #c9a43b;
  }
  * { box-sizing: border-box; margin: 0; padding: 0; }
  html, body { width: 1200px; height: 675px; overflow: hidden; }
  body { background: var(--backdrop); position: relative; font-family: "Poppins", sans-serif; }

  .cover {
    position: absolute; left: 50px; top: 97px; width: 1100px; height: 480px;
    background: var(--navy-dark); overflow: hidden;
  }
  .hero { position: absolute; left: 0; top: 0; width: 1100px; height: 316px; }
  .hero-scene {
    position: absolute; inset: 0;
    background: linear-gradient(180deg, var(--sky-top) 0%, var(--sky-mid) 45%, var(--dusk) 100%);
  }
  .hero-stripes { position: absolute; inset: 0; }
  .headshot {
    position: absolute; left: 652px; top: 26px; width: 343px; height: 290px;
    background: var(--portrait-tone);
  }

  .brand { position: absolute; left: 132px; top: 34px; display: flex; align-items: center; gap: 16px; }
  .brand-mark { width: 62px; height: 62px; border: 8px solid var(--ink); }
  .brand-name {
    font-family: "Montserrat", sans-serif; font-weight: 600; font-size: 45px;
    color: var(--ink); letter-spacing: 0.5px; line-height: 1;
  }
  .brand-title {
    font-family: "Montserrat", sans-serif; font-weight: 600; font-size: 12.5px;
    color: var(--ink); letter-spacing: 5.5px; margin-top: 6px; margin-left: 52px;
  }

  .info { position: absolute; left: 0; top: 316px; width: 1100px; height: 164px; }
  .affiliations { position: absolute; left: 38px; top: 18px; display: flex; align-items: center; height: 62px; }
  .brokerage { display: flex; align-items: center; gap: 6px; }
  .brokerage-square { width: 34px; height: 38px; background: var(--green); }
  .brokerage-name {
    font-family: "Poppins", sans-serif; font-weight: 700; font-size: 19px; line-height: 1.1;
    color: #e9e9e9; letter-spacing: 0.3px;
  }
  .divider { width: 1px; height: 58px; margin: 0 26px; border-left: 1px dashed var(--gold); }
  .badge { width: 124px; height: 42px; border-radius: 4px; background: #2a2c3a; }
  .badge-wide { width: 145px; }

  .phone {
    position: absolute; left: 628px; top: 19px; width: 432px; height: 67px;
    background: var(--green); border-radius: 8px;
    display: flex; align-items: center; justify-content: center;
    font-family: "Poppins", sans-serif; font-weight: 700; font-size: 52px; color: var(--white);
    letter-spacing: 0.5px; line-height: 1;
  }
  .contact-line {
    position: absolute; top: 98px; display: flex; align-items: center; gap: 12px;
    font-weight: 700; font-size: 27px; color: var(--white); white-space: nowrap; line-height: 1.3;
  }
  .contact-web { left: 42px; }
  .contact-mail { left: 549px; }
  .contact-icon { width: 24px; height: 24px; flex: none; }
</style>
</head>
<body>
  <main class="cover">
    <section class="hero">
      <div class="hero-scene" role="img" aria-label="Sunset over a row of green lakeside houses reflected in calm water"></div>
      <svg class="hero-stripes" width="1100" height="316" viewBox="0 0 1100 316" aria-hidden="true">
        <polygon points="728,0 838,0 712,316 645,316" fill="var(--green)" opacity="0.9"/>
        <polygon points="838,0 940,0 840,316 740,316" fill="var(--green-soft)" opacity="0.8"/>
        <polygon points="940,0 1047,0 945,316 850,316" fill="var(--green-deep)" opacity="0.9"/>
      </svg>
      <div class="headshot" role="img" aria-label="Headshot of the broker"></div>
      <div class="brand">
        <div class="brand-mark"></div>
        <div>
          <div class="brand-name">MARK DELANEY</div>
          <div class="brand-title">BROKER | REALTOR</div>
        </div>
      </div>
    </section>

    <section class="info">
      <div class="affiliations">
        <div class="brokerage">
          <div class="brokerage-square"></div>
          <div class="brokerage-name">HARBOR COVE<br>REALTY, INC.</div>
        </div>
        <div class="divider"></div>
        <div class="badge" role="img" aria-label="Luxury real estate network badge"></div>
        <div class="divider"></div>
        <div class="badge badge-wide" role="img" aria-label="Global real estate companies network badge"></div>
      </div>

      <div class="phone">555.014.2280</div>

      <div class="contact-line contact-web">
        <svg class="contact-icon" viewBox="0 0 24 24" aria-hidden="true">
          <circle cx="12" cy="12" r="12" fill="var(--green)"/>
          <g fill="none" stroke="var(--navy-dark)" stroke-width="1.4">
            <circle cx="12" cy="12" r="6.5"/>
            <ellipse cx="12" cy="12" rx="3" ry="6.5"/>
            <line x1="5.5" y1="12" x2="18.5" y2="12"/>
          </g>
        </svg>
        Mark Delaney Real Estate.com
      </div>
      <div class="contact-line contact-mail">
        <svg class="contact-icon" viewBox="0 0 24 24" aria-hidden="true">
          <circle cx="12" cy="12" r="12" fill="var(--green)"/>
          <rect x="6" y="8" width="12" height="8.5" fill="none" stroke="var(--navy-dark)" stroke-width="1.4"/>
          <polyline points="6,8 12,13 18,8" fill="none" stroke="var(--navy-dark)" stroke-width="1.4"/>
        </svg>
        MarkD@Harbor Cove Realty.com
      </div>
    </section>
  </main>
</body>
</html>
```